Pinecrest Real Estate A5 Flyer

A5 Flyer for print distribution.

Front (include attached photo and branding):
Pinecrest are a new face in the Shelley & Rossmoyne real estate market. The Pinecrest team are both Shelley ‘locals’ and are genuinely and sincerely committed to this community. They put people first and pursue exceptional outcomes for their clients. This is the founding vision of Pinecrest.

Values:
Outstanding Customer Service
Timely Communication
Integrity Always
People First
Exceptional Negotiation

If you’re thinking of selling, interested in a free market appraisal, or simply want to find out more about the Pinecrest team, please reach out to Doug or Rowan for a chat. We’d love to shout you a coffee at The Lantern Coffee + Kitchen.

Pinecrest Real Estate
E: hello@pinecrestrealestate-example.com.au
W: pinecrestrealestate-example.com.au

Back (half the page about Doug, other half the page about Rowan). Please include headshots (Rowan is the younger one):

Rowan Ferrabee (Property Consultant):

Rowan has an in-depth understanding of all things property & finance related. With a degree in property & finance, diploma in finance & mortgage broking, certificate IV in real estate practice, project management roles in residential property development, plus years of small business experience as co-founder/co-owner of The Lantern Coffee + Kitchen, his experience in managing competing demands and complex scenarios runs far and wide.

Rowan also has experience in corporate negotiations which is proving to be a very beneficial skill set. Rowan is deeply committed to people and pursuing exceptional outcomes for his clients. He has built a reputation as a man of his word who is genuine and sincere and willing to go above and beyond for his clients.

rowan@pinecrestrealestate-example.com.au
0412 306 248

Doug Penberthy (Director / Licensee):

Doug has worked in various roles inclusive of being a Real Estate Agent, Bank Manager, Financial Counsellor, Mortgage Broker, and previously a Commercial Pilot. He spent eight years in remote Western Australia, where he worked for an international mining company creating strategies to help support the well-being of employees. Doug’s focus in life has always been to help people. To him, it is always about the relationship. Doug gets enormous satisfaction from seeing individuals, families, and businesses thrive financially. He has become a skilled negotiator with extensive experience working for a number of corporations and private firms.
 
What differentiates Doug is his compassion and commitment to people. He works hard to be an excellent communicator with the aim of achieving great results. He  has extensive sales experience with incredible ability to push the boundaries, think outside the box and meet or surpass expectations. This is why his clients keep coming back and continue to refer well into the future. 

doug@pinecrestrealestate-example.com.au
0438 192 607

Target Market(s)

House Sellers / House Buyers

Industry/Entity Type

Real Estate

Colors
0054AA
0677BA
7BADD7
CADEEF
E8F1F8

Requirements
Must have
• Branding / logo, river photo, head shots, company details etc
Nice to have
• Design as per attached branding guide

```html
<!DOCTYPE html>
<html lang="en">
<head>
<meta charset="utf-8">
<title>Pinecrest Real Estate – A5 Flyer</title>
<link href="https://fonts.googleapis.com/css2?family=Montserrat:wght@400;500;600;800;900&display=swap" rel="stylesheet">
<style>
  :root{
    --navy:#1b2a3b;
    --navy-deep:#162332;
    --blue:#0677BA;
    --blue-strong:#0054AA;
    --blue-bright:#1b7fd0;
    --blue-soft:#7BADD7;
    --blue-pale:#CADEEF;
    --white:#ffffff;
    --ink:#1b2a3b;
    --line:#c9ced4;
  }
  *{margin:0;padding:0;box-sizing:border-box}
  html,body{width:893px;height:1200px;overflow:hidden;background:#fff}
  body{font-family:"Montserrat",sans-serif;color:var(--ink)}
  .flyer{position:relative;width:893px;height:1200px;background:var(--white);overflow:hidden}

  /* Brand */
  .brand{position:absolute;top:38px;left:0;width:100%;display:flex;justify-content:center;align-items:center;gap:22px}
  .brand-mark{width:88px;height:88px;border-radius:50%;background:var(--navy)}
  .brand-name{font-family:"Montserrat",sans-serif;font-weight:400;font-size:44px;letter-spacing:15px;color:var(--navy)}

  /* Photo area */
  .hero-photo{position:absolute;top:139px;left:0;width:100%;height:520px;
    background:
      linear-gradient(180deg,rgba(27,42,59,0) 62%,var(--navy) 100%),
      linear-gradient(100deg,#6f7f86 0%,#5d6f5c 30%,#3d5a74 48%,#2f5783 70%,#355f8c 100%),
      linear-gradient(180deg,#e6ecf1 0%,#dde6ec 12%,#b8c6cf 14%,transparent 20%);
    background-blend-mode:normal}
  .hero-photo::before{content:"";position:absolute;inset:0;
    background:linear-gradient(180deg,#eef2f5 0%,#dfe6eb 10%,rgba(223,230,235,0) 14%)}

  /* Dark panel */
  .panel{position:absolute;top:600px;left:0;width:100%;height:429px;background:var(--navy)}
  .intro{position:absolute;top:553px;left:0;width:100%;text-align:center;color:var(--white);
    font-size:18.5px;line-height:26px;font-weight:400}
  .headline{position:absolute;top:635px;left:0;width:100%;text-align:center;color:var(--blue-bright);
    font-weight:900;font-size:28.5px;line-height:35px;text-transform:uppercase;letter-spacing:.2px}
  .vision{position:absolute;top:712px;left:0;width:100%;text-align:center;color:var(--white);
    font-size:18px;font-weight:400;text-transform:uppercase}

  /* Values */
  .values{position:absolute;top:764px;left:75px;width:761px;height:170px;border:1.5px solid var(--white);border-radius:18px}
  .values-tab{position:absolute;top:21px;left:-15px;width:200px;height:42px;background:linear-gradient(90deg,var(--blue-strong),var(--blue-bright));
    border-radius:10px 6px 6px 0;color:var(--white);font-weight:800;font-size:18.5px;display:flex;align-items:center;justify-content:center;letter-spacing:.3px}
  .values-tab::after{content:"";position:absolute;left:0;bottom:-12px;border-top:12px solid #0b3d73;border-left:15px solid transparent}
  .value{position:absolute;display:flex;align-items:center}
  .value-icon{width:62px;height:62px;border-radius:50%;background:var(--blue);border:2.5px solid var(--white);box-shadow:0 0 0 2px var(--blue);display:flex;align-items:center;justify-content:center;flex:none}
  .value-icon svg{width:34px;height:34px}
  .value-label{margin-left:18px;color:var(--white);font-weight:500;font-size:16.5px;line-height:21px;text-transform:uppercase}
  .v1{left:214px;top:12px}
  .v2{left:500px;top:12px}
  .v3{left:23px;top:93px}
  .v3 .value-label{margin-left:10px}
  .v4{left:217px;top:93px}
  .v5{left:500px;top:93px}

  .cta{position:absolute;top:960px;left:0;width:100%;text-align:center;color:var(--white);font-size:18.5px;line-height:25px}

  .rule{position:absolute;top:1029px;left:0;width:100%;height:4px;background:var(--blue)}

  /* Footer */
  .contact-lines{position:absolute;top:1057px;left:0;width:100%}
  .reach{position:absolute;left:73px;top:0;display:flex;gap:14px}
  .coffee{position:absolute;left:415px;top:0;display:flex;gap:14px}
  .contact-lines svg{width:48px;height:48px;flex:none;margin-top:2px}
  .callout{font-weight:900;font-size:21px;line-height:25px;text-transform:uppercase;color:var(--navy)}
  .callout .accent{color:var(--blue-bright)}
  .links{position:absolute;top:1143px;left:70px;width:745px;height:35px;border:1.3px solid var(--line);border-radius:18px;
    display:flex;align-items:center;justify-content:space-around;font-size:16px;color:var(--navy)}
  .link{display:flex;align-items:center;gap:10px}
  .link svg{width:22px;height:22px}
</style>
</head>
<body>
<main class="flyer">
  <header class="brand">
    <span class="brand-mark"></span>
    <span class="brand-name">PINECREST</span>
  </header>

  <div class="hero-photo" role="img" aria-label="Aerial photograph of the Shelley riverfront: houses and trees along a road beside the river, boats on the water, city skyline in the distance"></div>

  <section class="panel"></section>

  <p class="intro">Pinecrest are a new face in the Shelley &amp; Rossmoyne Real<br>estate market. The Pinecrest team are both Shelley ‘locals’ and are<br>genuinely and sincerely committed to this community.</p>

  <h1 class="headline">They put people first and pursue<br>exceptional outcomes for their clients.</h1>
  <p class="vision">This is the founding vision of Pinecrest.</p>

  <section class="values">
    <div class="values-tab">OUR VALUES</div>

    <div class="value v1">
      <span class="value-icon"><svg viewBox="0 0 34 34" fill="none" stroke="#fff" stroke-width="1.8" stroke-linecap="round" stroke-linejoin="round"><circle cx="17" cy="11" r="6"/><path d="M14.5 11l2 2 3-3.5"/><path d="M13 16l-2 6 3-1 2 2M21 16l2 6-3-1-2 2"/><path d="M4 27h6l5 2h8l6-4"/></svg></span>
      <span class="value-label">Outstanding<br>customer service</span>
    </div>
    <div class="value v2">
      <span class="value-icon"><svg viewBox="0 0 34 34" fill="none" stroke="#fff" stroke-width="1.8" stroke-linecap="round" stroke-linejoin="round"><path d="M5 14h5l12-6v18l-12-6H5z"/><path d="M8 20l2 7h3l-1-7"/><circle cx="26" cy="17" r="3.5"/></svg></span>
      <span class="value-label">Timely<br>communication</span>
    </div>
    <div class="value v3">
      <span class="value-icon"><svg viewBox="0 0 34 34" fill="none" stroke="#fff" stroke-width="1.8" stroke-linecap="round" stroke-linejoin="round"><rect x="8" y="5" width="8" height="8" rx="1"/><rect x="18" y="5" width="8" height="8" rx="1"/><rect x="18" y="15" width="8" height="6" rx="1"/><path d="M4 28h6l5 1h7l6-5"/><path d="M4 22h5l5 2h4"/></svg></span>
      <span class="value-label">Integrity<br>always</span>
    </div>
    <div class="value v4">
      <span class="value-icon"><svg viewBox="0 0 34 34" fill="none" stroke="#fff" stroke-width="1.8" stroke-linecap="round" stroke-linejoin="round"><circle cx="19" cy="7" r="3"/><path d="M14 17c0-3 2-5 5-5s5 2 5 5z"/><path d="M4 21h5v9H4zM9 22h6l4 2h5l5-3v3l-6 5H9"/></svg></span>
      <span class="value-label">People first</span>
    </div>
    <div class="value v5">
      <span class="value-icon"><svg viewBox="0 0 34 34" fill="none" stroke="#fff" stroke-width="1.8" stroke-linecap="round" stroke-linejoin="round"><path d="M17 3v4M10 5l2 3M24 5l-2 3"/><path d="M3 16l5-4 5 2 4-2 5 1 6 3-3 6"/><path d="M3 16l4 6 6 5 4 1 3-2 5-2"/><path d="M13 19l4 4M16 17l4 4"/></svg></span>
      <span class="value-label">Exceptional<br>negotiation</span>
    </div>
  </section>

  <p class="cta">If you’re thinking of selling, interested in a free market appraisal, or<br>simply want to find out more about the Pinecrest team,</p>

  <div class="rule"></div>

  <section class="contact-lines">
    <div class="reach">
      <svg viewBox="0 0 48 48" fill="none" stroke="#1b2a3b" stroke-width="2.4" stroke-linecap="round" stroke-linejoin="round"><path d="M4 8h32v22H16l-8 6v-6H4z"/><circle cx="13" cy="19" r="1.3" fill="#1b2a3b"/><circle cx="20" cy="19" r="1.3" fill="#1b2a3b"/><circle cx="27" cy="19" r="1.3" fill="#1b2a3b"/><path d="M40 16h4v20h-4v5l-7-5H22" stroke="#1b7fd0"/></svg>
      <p class="callout">Please reach out<br>to <span class="accent">Doug</span> or <span class="accent">Rowan</span><br>for a chat.</p>
    </div>
    <div class="coffee">
      <svg viewBox="0 0 48 48" fill="none" stroke="#1b2a3b" stroke-width="2.4" stroke-linecap="round" stroke-linejoin="round"><path d="M16 4c-2 2 2 4 0 6M22 4c-2 2 2 4 0 6M28 4c-2 2 2 4 0 6" stroke="#1b7fd0"/><path d="M9 16h28v10c0 7-6 12-14 12S9 33 9 26z"/><path d="M37 19h4a4 4 0 010 8h-5"/><path d="M3 43h40"/></svg>
      <p class="callout">We’d love to shout you<br>a coffee at The Lantern<br><span class="accent">Coffee + Kitchen.</span></p>
    </div>
  </section>

  <footer class="links">
    <span class="link"><svg viewBox="0 0 22 22" fill="none" stroke="#1b7fd0" stroke-width="2" stroke-linejoin="round"><rect x="2" y="4" width="18" height="14" rx="1"/><path d="M2 5l9 7 9-7"/></svg>hello@pinecrestrealestate-example.com.au</span>
    <span class="link"><svg viewBox="0 0 22 22" fill="none" stroke="#1b7fd0" stroke-width="1.8"><circle cx="11" cy="11" r="9"/><ellipse cx="11" cy="11" rx="4" ry="9"/><path d="M2 11h18"/></svg>pinecrestrealestate-example.com.au</span>
  </footer>
</main>
</body>
</html>
```